Design needed for Cover of Conference Brochure

We are a conference company that puts on several business conferences per year. We are putting together a new conference - the Brightpath Insight Forum, and our audience is UX practitioners and specialists, product designers, UX designers, etc.
We need a brochure cover created. We are looking for fresh design ideas and are open to varying color schemes - please just keep in mind that this is a conference for business professionals, and fonts and colors should reflect this. Only restriction is that we do have a general cover format that we follow - i.e. which text goes where. (I've attached samples from our other events to reference.) We also generally have a central image to each brochure - feel free to submit a few versions with different images... we want something that accurately represents UX. However, if the design is compelling enough, image might not be completely necessary. We are relatively flexible - we just want something sharp!
- Must include KLVO logo (see placing on sample event covers)
- Must include footer - see sample covers
- Red text in word document are notes to you the designer - not actual text meant to appear on the cover
This cover is standard 8x11, and will be used for web only, not print. I have attached a word doc that includes all of the text that you will need for the cover. We will need final version in PDF, jpeg, and PSD. Please message me with any questions or clarification.

```html
<!DOCTYPE html>
<html lang="en">
<head>
<meta charset="utf-8">
<title>Brightpath Insight Forum – Brochure Cover</title>
<link href="https://fonts.googleapis.com/css2?family=Lilita+One&family=Mulish:wght@400;700;800&family=Roboto+Condensed:wght@400;500&family=Oswald:wght@600&display=swap" rel="stylesheet">
<style>
  :root{
    --paper:#fbf8ea;
    --paper-line:#e9e5d2;
    --teal-dark:#1f4d55;
    --teal:#3f7379;
    --yellow:#ffe21a;
    --title-blue:#2a7fd0;
    --navy:#1c1d6e;
    --bullet-blue:#2b2a8f;
    --red:#c8202c;
    --white:#ffffff;
    --art-cream:#efe3cd;
    --art-teal:#8fb2b0;
  }
  *{margin:0;padding:0;box-sizing:border-box}
  html,body{width:946px;height:1200px;overflow:hidden;background:var(--paper)}
  .cover{
    position:relative;width:946px;height:1200px;overflow:hidden;
    background:repeating-linear-gradient(to bottom,var(--paper) 0 7px,var(--paper-line) 7px 8px);
    font-family:"Mulish",sans-serif;
  }
  .bands{position:absolute;inset:0;width:946px;height:1200px}
  .event-title{
    position:absolute;top:74px;left:0;width:946px;text-align:center;
    font-family:"Lilita One",sans-serif;font-weight:400;font-size:56px;letter-spacing:1px;
    color:var(--navy);
    -webkit-text-stroke:7px var(--white);paint-order:stroke fill;
    text-shadow:
      3px 0 0 var(--title-blue),-3px 0 0 var(--title-blue),0 3px 0 var(--title-blue),0 -3px 0 var(--title-blue),
      3px 3px 0 var(--title-blue),-3px -3px 0 var(--title-blue),3px -3px 0 var(--title-blue),-3px 3px 0 var(--title-blue),
      6px 0 0 var(--yellow),-6px 0 0 var(--yellow),0 6px 0 var(--yellow),0 -6px 0 var(--yellow),
      5px 5px 0 var(--yellow),-5px -5px 0 var(--yellow),5px -5px 0 var(--yellow),-5px 5px 0 var(--yellow);
  }
  .event-info{
    position:absolute;top:222px;left:0;width:356px;height:106px;
    background:linear-gradient(90deg,var(--teal) 0%,var(--teal-dark) 100%);
    border-radius:0 44px 44px 0;padding:16px 0 0 42px;color:var(--yellow);
    box-shadow:2px 3px 6px rgba(0,0,0,.25);
  }
  .event-date{font-weight:700;font-size:22px;margin-bottom:6px}
  .event-venue{font-size:16px;line-height:1.25}
  .tagline{
    position:absolute;top:236px;left:402px;width:530px;
    color:var(--red);font-weight:800;font-size:30px;line-height:1.3;
  }
  .feature-art{
    position:absolute;top:342px;left:96px;width:756px;height:410px;border-radius:50%;
    background:radial-gradient(ellipse at 50% 50%,var(--art-cream) 0%,var(--art-cream) 45%,var(--art-teal) 100%);
    box-shadow:0 3px 8px rgba(0,0,0,.2);
  }
  .highlights{position:absolute;top:784px;left:87px;list-style:none}
  .highlights li{
    display:flex;align-items:center;gap:8px;height:42.5px;
    font-family:"Roboto Condensed",sans-serif;font-weight:500;font-size:24px;color:var(--bullet-blue);
  }
  .tick{width:28px;height:24px;flex:none}
  .early-bird{
    position:absolute;top:968px;left:46px;width:400px;height:126px;border-radius:50%;
    background:radial-gradient(ellipse at 50% 40%,#fff3b8 0%,#f2c94a 55%,#d79b1e 100%);
    border:6px solid #d87a2a;text-align:center;padding-top:26px;
    box-shadow:0 3px 6px rgba(0,0,0,.25);
  }
  .early-bird-note{font-family:"Roboto Condensed",sans-serif;font-size:20px;color:var(--navy)}
  .early-bird-offer{font-family:"Oswald",sans-serif;font-weight:600;font-size:38px;color:var(--red);line-height:1.15}
  .organizer{
    position:absolute;top:1028px;left:730px;display:flex;align-items:center;gap:10px;
  }
  .organizer-mark{width:34px;height:34px;background:#2a8fd6}
  .organizer-name{font-weight:800;font-size:34px;color:var(--navy)}
  .register-cta{
    position:absolute;top:1143px;left:36px;
    font-family:"Roboto Condensed",sans-serif;font-weight:500;font-size:28px;color:var(--yellow);
  }
  .contact{position:absolute;top:1118px;right:38px;text-align:right;color:var(--white)}
  .contact-phone{font-weight:800;font-size:31px;display:flex;align-items:center;gap:6px;justify-content:flex-end}
  .contact-web{font-size:15px;display:flex;align-items:center;gap:6px;justify-content:flex-end;margin-top:4px}
  .contact svg{flex:none}
</style>
</head>
<body>
<main class="cover">
  <svg class="bands" viewBox="0 0 946 1200" aria-hidden="true">
    <defs>
      <linearGradient id="goldBand" x1="0" x2="1" y1="0" y2="0">
        <stop offset="0" stop-color="#a98240"/>
        <stop offset=".45" stop-color="#e2c57e"/>
        <stop offset="1" stop-color="#c2842c"/>
      </linearGradient>
      <linearGradient id="brownBand" x1="0" x2="1" y1="0" y2="0">
        <stop offset="0" stop-color="#6b3f16"/>
        <stop offset=".45" stop-color="#3f260d"/>
        <stop offset="1" stop-color="#a06c2c"/>
      </linearGradient>
      <linearGradient id="silverBand" x1="0" x2="1">
        <stop offset="0" stop-color="#ffffff"/>
        <stop offset=".6" stop-color="#c3c5ca"/>
        <stop offset="1" stop-color="#8f9298"/>
      </linearGradient>
    </defs>
    <path d="M0 0H946V232C860 190 700 188 520 196C330 204 140 196 0 172Z" fill="url(#silverBand)"/>
    <path d="M0 0H946V214C860 184 700 182 520 190C330 198 140 190 0 166Z" fill="url(#goldBand)"/>
    <path d="M0 1060C180 1080 420 1086 640 1070C780 1060 880 1054 946 1054V1200H0Z" fill="url(#silverBand)"/>
    <path d="M0 1090C200 1098 430 1094 640 1080C780 1070 880 1064 946 1064V1200H0Z" fill="url(#brownBand)"/>
  </svg>

  <h1 class="event-title">BRIGHTPATH INSIGHT FORUM</h1>

  <section class="event-info">
    <p class="event-date">June 10-12, 2014</p>
    <p class="event-venue">Harborview Club &amp; Hotel<br>San Francisco, CA</p>
  </section>

  <h2 class="tagline">Design Compelling Experiences through Successful UX Strategy</h2>

  <div class="feature-art" role="img" aria-label="Oval illustration: two profile silhouettes facing each other with gears in their heads, overlapping speech bubbles with a light bulb, and a small grid chart between them"></div>

  <ul class="highlights">
    <li><svg class="tick" viewBox="0 0 28 24"><rect x="1" y="6" width="17" height="16" fill="none" stroke="#2b2a8f" stroke-width="2"/><path d="M5 13l5 6L26 2" fill="none" stroke="#c8202c" stroke-width="4" stroke-linecap="round" stroke-linejoin="round"/></svg>Case Studies from Leading Brands on Executing an Effective UX Strategy</li>
    <li><svg class="tick" viewBox="0 0 28 24"><rect x="1" y="6" width="17" height="16" fill="none" stroke="#2b2a8f" stroke-width="2"/><path d="M5 13l5 6L26 2" fill="none" stroke="#c8202c" stroke-width="4" stroke-linecap="round" stroke-linejoin="round"/></svg>Learn How UX-Driven Innovation Can Change Your Business</li>
    <li><svg class="tick" viewBox="0 0 28 24"><rect x="1" y="6" width="17" height="16" fill="none" stroke="#2b2a8f" stroke-width="2"/><path d="M5 13l5 6L26 2" fill="none" stroke="#c8202c" stroke-width="4" stroke-linecap="round" stroke-linejoin="round"/></svg>Build a Successful UX Team that Operates Strategically</li>
    <li><svg class="tick" viewBox="0 0 28 24"><rect x="1" y="6" width="17" height="16" fill="none" stroke="#2b2a8f" stroke-width="2"/><path d="M5 13l5 6L26 2" fill="none" stroke="#c8202c" stroke-width="4" stroke-linecap="round" stroke-linejoin="round"/></svg>Insights into UX Research, User Behavior, Usability Testing, Lean UX, and More</li>
  </ul>

  <div class="early-bird">
    <p class="early-bird-note">Register by March 7th, 2014 and</p>
    <p class="early-bird-offer">save $400!</p>
  </div>

  <div class="organizer">
    <span class="organizer-mark"></span>
    <span class="organizer-name">KLVO</span>
  </div>

  <p class="register-cta">Register Today!</p>

  <div class="contact">
    <p class="contact-phone"><svg width="26" height="26" viewBox="0 0 26 26"><circle cx="13" cy="13" r="11.5" fill="none" stroke="#fff" stroke-width="2"/><path d="M9 6c-2 1-2 4 0 8s5 6 7 6l2-2-3-3-2 1c-1-1-2-2-3-4l1-2-2-4z" fill="#fff"/></svg>888.555.0142</p>
    <p class="contact-web"><svg width="16" height="16" viewBox="0 0 16 16"><circle cx="8" cy="8" r="7" fill="none" stroke="#fff" stroke-width="1.2"/><ellipse cx="8" cy="8" rx="3" ry="7" fill="none" stroke="#fff" stroke-width="1"/><path d="M1 8h14M2.5 4.5h11M2.5 11.5h11" stroke="#fff" stroke-width="1"/></svg>www.brightpathforum.com</p>
  </div>
</main>
</body>
</html>
```